Modern, crisp, funky web 2.0 site required for childrens holiday programmes

We want a new "Wow" website. Please help this become a reality.

Funtrek is a provider of childrens holiday programmes aimed primary at children 5yrs to 12 yrs. You can view our current site at www.funtrek.co.nz

This website is a primarily a booking portal. Parents typically come to the website to register and book for courses after having seen them in a booklet. However we are changing the marketing approach and are now trying to attract parents directly to the website. Therefore we want the website to be very graphically appealing, very easy to browse and navigate and must be easy to register and book.

The front end is what is being re-designed. The new front end MUST be compatible with the existing back-end system and processes and the back-end should not need to be changed at all. People lodging a tender must familiarise themselves with the existing site and ensure that the new front end will be fully compatible.

The site must be PHP

This tender will not include a re-design of the logo. Please use the current logo which is attached with this document.

Everything else is up for re-design. The site needs a new, clean, crisp modern design. (See Likes and Dislikes).

Some yellow must be used somewhere within the colour scheme to be in keeping with the brand colours. However no yellow background please.

We currently operate in 2 main regions: Auckland and Palmerston North. However we will be adding new regions soon. The website should make it easy for users to find courses in their region easily.

We also offer term time activities – the site needs another area for that. Perhaps emulated as another “region”.

Beyond that courses are offered across a range of activities. Ideally the website would organise courses logically so that users can find what they are looking for easily.

However, if possible it would be good for the user to be able to browse by area. For example within Auckland there would be North Shore, Central, West, East and South. Within each area a range of course are available – e.g. Skateboarding, Surfing etc. However we don’t want this to be the primary design goal. This is more a “could have” than a “must have”

Once the user has found the course they want the site needs to have a course identification button / tab / box e.g. Tennis. Once the user has clicked through all the details pertaining to the tennis courses on offer should be presented. People are used to searching the existing website in this manner.

When clients click through from the course they have chosen to book the GREEN box that’s say “More Info” needs to be changed to say Book Now

Needs to the ability to have photos displayed on each page next to course descriptions or a panel of photos showing the children doing the activity displayed on that page.

Needs the ability to select the “Pick up locations” To show up in the booking form and class attendance sheet e.g. 7.45am/4.45pm: Harbourview Burgerbarn Carpark. In front of Burgerbarn by the shopping trundler bay.
8.10am/4.10pm: Tolley Cove Reserve, Ridgefield Road, Marlowton in the car park in form of the tennis courts

Needs to have Course options above the line (at the top of the page)

Needs to have a description of Funtrek below the line (at the bottom of the page)

You can provide stock images but they must be New Zealand activities (i.e. not American Football) and pre-approved by us. Alternatively we can supply some images.

What adjectives should best describe your website design?
Clean, modern, professional, vibrant, both kid and adult appealing, fun, interesting

What content must be included in the website design?

• Home page
• Contact us
• Testimonials
• Terms and conditions
• New customer sign or log in
• My account or existing client log in
• Chatterbook button,
• Sign up to the newsletter (postparrot)
• Refer a friend option – where they input a friend’s contact details, we then send them a one-off email “from” the friend with a HTML email describing our website. Content of the email must be able to be modified easily later (by a programmer).
• “Become a course provider” enquiry tab. This could be a simple form which emails details through.
• Have “View latest booklet” tab which downloads a PDF of the booklet after submitting the users email address onto our PostParrot mailing list (must offer postparrot integration).
• Must support Zenmetric analytics data collection
Updates

Reason: I have not really seen anything that greatly excites me. I am concerned we re not getting the level of design work in as committed to on the starting up stage we only have 18 designs (Many from the same designer and repeats) I was expecting closer to 50. Please can you assist and advise as to how to improve the results thanks Dana

Target Market(s)

Parents, both working and stay at home, children aged 5-15 years of age with middle – high income.

Industry/Entity Type

Marketing

Requirements
Must have
• The site must be easy to use and navigate.

Users need to be able to navigate with the minimal number of clicks as the site is used by busy mums with no patience!

Users should be able to find exactly what they want with absolute ease.

Needs to be appealing to children aged 5 – 12 years old as well as parents of children within that age range.

Needs to have lots of images of children doing the activities offered. Should NOT have cartoon images!

Must be able to written in PHP – this is to enable it to be compatible with the existing back-end.

Likes:

Big Icons
Clean, crisp design
Vivid, striking in appearance
Uncluttered
Easy to navigate
Social Media integration
Modern
Not much ‘below the line’
Thematically consistent
Easily modifiable pictures and content
Like real images
Search bar would be good if effective ONLY

What colours do you want to see in your website design?
The Yellow in the logo BUT NOT as the background, purple as in the balls etc on logo, white for clean and simple easy to read, black for writing and other areas for details ie boarders etc.
Should not have
• Dislikes:

Cartoon images – must be real images.
Moving, floating in and out and spinning pictures text or photos
Clutter
Underlining
Intentionally misspelt words and typos
Content ‘below the line’ on the Home page
Backgrounds ending before the edge of the screen

What colours do you NOT want to see in your website design?
Browns, pink, pastel colours, mustard, pale yellow, and not a confusion of colours – must be themed and consistent.

```html
<!DOCTYPE html>
<html lang="en">
<head>
<meta charset="utf-8">
<title>Funtrek – Horse Riding</title>
<link rel="stylesheet" href="https://fonts.googleapis.com/css2?family=Arimo:wght@400;700&family=Oswald:wght@500;600&display=swap">
<style>
:root{
  --paper:#f2f1ee;
  --white:#ffffff;
  --purple:#6b3ea0;
  --purple-dark:#5a2f8c;
  --purple-light:#ddd3e8;
  --yellow:#e9e21f;
  --ink:#1b1b1b;
  --muted:#555;
  --field:#f4f4f4;
  --line:#bdbdbd;
}
*{box-sizing:border-box;margin:0;padding:0}
html,body{width:1053px;height:1200px;overflow:hidden}
body{background:var(--paper);font-family:"Arimo",Arial,sans-serif;color:var(--ink);position:relative}
.abs{position:absolute}

/* header */
.brand{left:88px;top:22px}
.brand-name{display:flex;align-items:center;gap:8px;font:700 44px/1 "Arimo",Arial,sans-serif;color:var(--ink);letter-spacing:-1px}
.brand-dot{width:22px;height:22px;border-radius:50%;background:var(--yellow)}
.brand-tag{font-size:12.5px;color:#333;margin:10px 0 0 38px;letter-spacing:.2px}
.account-links{right:90px;top:13px;font-size:13.5px;color:#222}
.social{right:90px;top:94px;display:flex;gap:22px;font-size:11px;color:#222;align-items:center}
.social .nets{display:flex;gap:8px;color:var(--purple);font-weight:700}

/* nav */
.nav{left:0;top:127px;width:1053px;height:44px;background:var(--purple);display:flex;align-items:center;padding-left:88px}
.nav a{color:var(--white);text-decoration:none;font-size:15.5px;height:44px;line-height:44px;padding:0 11px;margin-right:7px}
.nav a.active{background:var(--purple-dark)}

/* hero */
.hero{left:82px;top:177px;width:885px;height:588px;background:linear-gradient(160deg,#6f7a3c 0%,#9a9b5a 35%,#b84050 55%,#7c8a48 75%,#3f4a26 100%)}
.hero-title{right:86px;top:199px;width:233px;height:52px;background:rgba(244,243,240,.95);font:600 29px/52px "Oswald",sans-serif;color:var(--purple);text-align:center;letter-spacing:.5px}

/* search panel */
.panel{background:var(--white);box-shadow:0 0 4px rgba(0,0,0,.12)}
.search{left:92px;top:618px;width:202px;height:292px;padding:10px 12px}
.panel-title{font:500 15px/1 "Oswald",sans-serif;color:var(--ink);text-transform:uppercase;letter-spacing:.2px}
.field-label{font-size:12px;position:absolute;left:13px}
.select{position:absolute;height:19px;border:1px solid var(--line);background:var(--field);font-size:11.5px;color:#555;line-height:17px;padding-left:4px}
.select::after{content:"";position:absolute;right:0;top:0;width:18px;height:17px;border-left:1px solid var(--line);background:#e6e6e6}
.select .arrow{position:absolute;right:5px;top:6px;border:4px solid transparent;border-top:6px solid #888;z-index:1}
.date .cal{position:absolute;right:3px;top:4px;width:9px;height:9px;border:1px solid #777;z-index:1}
.btn{background:var(--purple);color:var(--white);font-weight:700;text-align:center}
.filter{left:12px;top:256px;width:177px;height:20px;font-size:12px;line-height:20px}

/* newsletter */
.newsletter{left:95px;top:921px;width:200px;height:76px;background:var(--purple);padding:8px 12px;color:var(--white)}
.newsletter .panel-title{color:var(--white)}
.newsletter .email{position:absolute;left:9px;top:29px;width:181px;height:20px;background:var(--white);border:1px solid #cfc6db}
.newsletter .hint{position:absolute;left:11px;top:56px;font-size:12px}
.newsletter .submit{position:absolute;right:16px;top:56px;background:var(--white);color:var(--ink);font-size:10px;padding:1px 7px;border-radius:8px}

/* phones */
.phones{left:95px;top:1010px;width:200px;height:120px;background:rgba(255,255,255,.55);padding:6px 0 0 21px}
.region{font-size:15.5px;color:#333}
.phone{display:flex;align-items:center;gap:6px;font-size:21px;color:#222;margin:2px 0 10px -6px}

/* course detail */
.course{left:305px;top:618px;width:650px;height:477px;padding:10px 22px}
.course h1{font:500 15px/1.2 "Oswald",sans-serif;text-transform:uppercase;letter-spacing:.2px}
.course p{font-size:12px;line-height:15px;text-align:justify;margin-top:16px}
.row{position:absolute;left:22px;font-size:12px}
.row .val{position:absolute;left:126px;white-space:nowrap}
.session{position:absolute;left:140px;width:467px;height:55px;background:var(--purple-light);font-size:12px;line-height:15px;padding:4px 9px}
.tick{position:absolute;right:13px;top:18px;width:20px;height:19px;background:var(--white);border:1px solid #aaa}
.book{position:absolute;left:533px;top:412px;width:74px;height:24px;line-height:24px;font-size:12.5px;font-weight:400}
.note{position:absolute;left:22px;top:454px;font-size:12px}

/* footer */
.foot-links{left:94px;top:1151px;font-size:12px}
.foot-rule{left:94px;top:1170px;width:862px;height:1px;background:#555}
.foot-text{left:94px;top:1174px;font-size:12px}
</style>
</head>
<body>

<header>
  <div class="abs brand">
    <div class="brand-name"><span class="brand-dot"></span>Funtrek</div>
    <div class="brand-tag">A WORLD OF FUN ACTIVITIES</div>
  </div>
  <div class="abs account-links">Log in I Register I My Account I Shopping Cart</div>
  <div class="abs social">
    <span>Tell a Friend About Us</span>
    <span>Follow Us</span>
    <span class="nets"><span>Chatterbook</span><span>Viewtube</span><span>Circlenet</span></span>
  </div>
</header>

<nav class="abs nav">
  <a href="#">HOME</a>
  <a href="#" class="active">COURSES</a>
  <a href="#">TESTIMONIALS</a>
  <a href="#">TERMS AND CONDITIONS</a>
  <a href="#">BECOME A COURSE PROVIDER</a>
  <a href="#">CONTACT</a>
</nav>

<div class="abs hero" role="img" aria-label="Photo of a girl in a riding helmet and red jacket riding a grey pony beside a paddock fence"></div>
<div class="abs hero-title">HORSE RIDING</div>

<section class="abs panel search">
  <div class="panel-title">Search &amp; Book a Course</div>
  <div class="field-label" style="top:42px">Location:</div>
  <div class="select" style="left:13px;top:55px;width:176px">Auckland<span class="arrow"></span></div>
  <div class="field-label" style="top:95px">Duration:</div>
  <div class="select" style="left:78px;top:86px;width:42px">3<span class="arrow"></span></div>
  <div class="field-label" style="top:123px">Start date:</div>
  <div class="select date" style="left:78px;top:115px;width:111px;padding-left:13px">09.07.2012<span class="cal"></span></div>
  <div class="field-label" style="top:151px">End date:</div>
  <div class="select date" style="left:78px;top:143px;width:111px;padding-left:13px">11.07.2010<span class="cal"></span></div>
  <div class="field-label" style="top:172px">Select a course:</div>
  <div class="select" style="left:13px;top:190px;width:176px">Horseriding Brookvale Riding<span class="arrow"></span></div>
  <div class="field-label" style="top:225px">Ages:</div>
  <div class="select" style="left:78px;top:222px;width:42px">6+<span class="arrow"></span></div>
  <div class="abs btn filter">Filter Courses</div>
</section>

<section class="abs newsletter">
  <div class="panel-title">Newsletter Sign Up</div>
  <div class="email"></div>
  <div class="hint">Enter your email</div>
  <div class="submit">Submit</div>
</section>

<section class="abs phones">
  <div class="region">Auckland</div>
  <div class="phone"><svg width="27" height="27" viewBox="0 0 27 27"><circle cx="13.5" cy="13.5" r="12" fill="none" stroke="#222" stroke-width="1.5"/><path d="M9 7c-1.5 1-2 3-1 5.5 1.3 3 3.5 5.5 6.5 7 2 1 3.5.6 4.5-.7l-2.3-2.3-1.7 1c-1.6-.8-3.3-2.6-4.2-4.3l1-1.7L9.5 7z" fill="#222"/></svg>555 0142</div>
  <div class="region">Palmerston North</div>
  <div class="phone"><svg width="27" height="27" viewBox="0 0 27 27"><circle cx="13.5" cy="13.5" r="12" fill="none" stroke="#222" stroke-width="1.5"/><path d="M9 7c-1.5 1-2 3-1 5.5 1.3 3 3.5 5.5 6.5 7 2 1 3.5.6 4.5-.7l-2.3-2.3-1.7 1c-1.6-.8-3.3-2.6-4.2-4.3l1-1.7L9.5 7z" fill="#222"/></svg>555 0187</div>
</section>

<main class="abs panel course">
  <h1>Brookvale Riding School: Own a Pony for 3 Days</h1>
  <p>This fantastic course is packed with horsemastership lessons, demonstrations and of course riding lessons! Meet the veterinarian and the farrier to learn about their work with horses. All levels of riders are catered for and children will be split into small groups depending on experience. As well as lessons, you will play mounted games, ride across country and learn to jump on your adopted pony. On the last day of the course you and your pony can test your skills against your friends and win ribbons in our gymkana. Workbooks are provided for you to keep.</p>
  <p style="margin-top:15px">Full time tuition is provided by professional equestrian coaches with top quality ponies and horses.</p>

  <div class="row" style="top:181px">Ages:<span class="val">6+</span></div>
  <div class="row" style="top:210px">Number of Places:<span class="val">20</span></div>
  <div class="row" style="top:240px">Instructor:<span class="val">Brookvale Riding School</span></div>
  <div class="row" style="top:269px;line-height:15px">Date, Time<br>and Venue:</div>

  <div class="session" style="top:288px">9-Jul-2012 to 11-Jul-2012<br>9:00 am to 3:00 pm<br>Brookvale Riding School, 14 Harlow Road, RD 3, Tarrowby
    <span class="tick"><svg width="18" height="17" viewBox="0 0 18 17"><path d="M5 9l3 3 5-7" fill="none" stroke="#333" stroke-width="1.6"/></svg></span>
  </div>
  <div class="session" style="top:349px">10-Jul-2012 to 12-Jul-2012<br>9:00 am to 3:00 pm<br>Brookvale Riding School, 14 Harlow Road, RD 3, Tarrowby
    <span class="tick"></span>
  </div>

  <div class="row" style="top:418px">Cost:<span class="val">$330.00</span></div>
  <div class="btn book">BOOK</div>
  <div class="note">Please select the date and venue of your choice and click on the book button to proceed.</div>
</main>

<footer>
  <div class="abs foot-links">Impressum I Terms and Conditions I Contact Us</div>
  <div class="abs foot-rule"></div>
  <div class="abs foot-text">We accept Paycard and Cardsure. For more assistance please contact us at: enquiries@funtrek.co.nz or call Auckland: 555 0142, Palmerston North: 555 0187</div>
</footer>

</body>
</html>
```